CCTV Security Product / Editable Infographic

I need a page designed to display a cctv system package.
The design will be in html so that it can be uploaded to a magento web page.
It will highlight the following features:
- 2 Year Warranty
- Plug & Play Technology - includes everything needed for setup
- Free Telephone Support
- Smartphone Compatible
- Silent Running
- True Colours
- Suitable for indoor or outdoor use
- Highlight the fact that it is a quality product and the best available in the market

The page will go here http://www.brovalemount.org.uk/cctv-systems.html so please make sure that it fits in with the website design.

The design should incorporate the attached camera and dvr and I will need to be able to change these images for others with the same dimensions.

If possible the design should have some sort of interactive element e.g. with jquery or html5 but this is definitely not essential and good design will take preference.

Many thanks

```html
<!DOCTYPE html>
<html lang="en">
<head>
<meta charset="utf-8">
<title>Brovale CCTV – CCTV Camera Systems</title>
<link rel="stylesheet" href="https://fonts.googleapis.com/css2?family=Lato:ital,wght@0,400;0,700;0,900;1,400;1,700&family=Oswald:wght@500;600&family=Playball&display=swap">
<style>
:root{
  --blue:#0b5cb5;
  --blue-dark:#0a4a94;
  --blue-light:#2a7fd4;
  --icon-blue:#1a5ca6;
  --ink:#333;
  --ink-soft:#555;
  --grey-bg:#ececec;
  --tile-bg:#e9e9ea;
  --line:#d6d6d6;
  --footer:#151515;
  --footer-low:#1f1f1f;
  --footer-base:#0b0b0b;
  --field:#2a2a2a;
  --white:#fff;
}
*{box-sizing:border-box;margin:0;padding:0}
html,body{width:1200px;height:2662px;overflow:hidden}
body{font-family:"Lato",Arial,sans-serif;color:var(--ink);background:var(--white);position:relative}
a{color:inherit;text-decoration:none}

/* top links */
.toplinks{position:absolute;top:0;left:0;width:1200px;height:38px;background:#f3f3f3;border-bottom:1px solid #e2e2e2}
.toplinks ul{list-style:none;position:absolute;right:135px;top:0;display:flex;height:38px}
.toplinks li{font-size:14px;line-height:38px;padding:0 22px;border-left:1px solid #ddd;color:#333}
.toplinks li:first-child{border-left:0;color:var(--blue)}

/* header */
.header{position:absolute;top:38px;left:0;width:1200px;height:113px;background:var(--white)}
.brand{position:absolute;left:135px;top:26px;display:flex;align-items:center;gap:14px}
.brand-square{width:58px;height:58px;background:var(--blue);border-radius:6px}
.brand-name{font-weight:900;font-size:34px;color:#1b1b1b;letter-spacing:.5px}
.hotline{position:absolute;left:603px;top:32px;display:flex;align-items:center;gap:10px}
.hotline-num{font-size:22px;font-weight:700;color:var(--blue);line-height:1;white-space:nowrap}
.hotline-hours{font-size:12px;font-weight:700;color:#222;margin-top:3px}
.search{position:absolute;left:823px;top:35px;width:242px;height:42px;border:1px solid #ccc;background:#f2f2f2;font-size:13px;font-style:italic;color:#555;padding:13px 12px}
.search svg{position:absolute;right:12px;top:13px}

/* main nav */
.mainnav{position:absolute;top:151px;left:0;width:1200px;height:49px;background:var(--blue)}
.mainnav ul{list-style:none;position:absolute;left:135px;top:0;width:765px;display:flex;height:49px;white-space:nowrap}
.mainnav li{color:var(--white);font-size:12.5px;font-weight:700;line-height:49px;padding:0 18px;letter-spacing:.2px}
.mainnav li.active{background:var(--blue-dark)}
.cart{position:absolute;left:909px;top:0;width:156px;height:49px;background:var(--blue-light);color:var(--white);font-size:15px;font-weight:700;display:flex;align-items:center;gap:10px;padding-left:14px;white-space:nowrap}

/* hero */
.hero{position:absolute;top:200px;left:0;width:1200px;height:377px}
.hero-photo{position:absolute;inset:0;background:linear-gradient(100deg,#cfc6bb 0%,#e6ded3 30%,#d9d6d2 55%,#bdbab6 80%,#a9a7a4 100%)}
.hero-camera{position:absolute;left:700px;top:20px;width:390px;height:240px;border-radius:60px 40px 40px 120px;background:radial-gradient(circle at 40% 55%,#4a4e54 0%,#2c2f33 55%,#3b3e42 100%)}
.hero-card{position:absolute;left:135px;top:106px;width:448px;height:204px;background:rgba(255,255,255,.93);padding:20px 18px}
.hero-card:after{content:"";position:absolute;right:0;top:0;border-top:14px solid var(--blue);border-left:14px solid transparent}
.hero-kicker{font-size:34px;line-height:1.1;white-space:nowrap}
.hero-kicker .script{font-family:"Playball",cursive;color:#222}
.hero-kicker .accent{font-family:"Lato",sans-serif;color:var(--blue);font-weight:400}
.hero-title{font-family:"Oswald",sans-serif;font-weight:600;font-size:39px;color:var(--blue);line-height:1.25;white-space:nowrap}
.hero-text{font-size:17px;line-height:1.55;color:#222;margin-top:4px}

/* intro */
.intro{position:absolute;top:577px;left:0;width:1200px;height:162px;background:linear-gradient(#fff,#f1f1f1);border-bottom:2px solid #e0e0e0}
.intro p{position:absolute;left:135px;top:22px;width:930px;text-align:center;font-size:21.5px;line-height:37px;color:#555}

/* benefits */
.benefits{position:absolute;top:741px;left:0;width:1200px;height:299px;background:var(--white);border-bottom:2px solid #dedede}
.section-title{font-size:28px;font-weight:700;color:#222;text-align:center}
.section-title span{color:var(--blue)}
.benefits .section-title{position:absolute;top:22px;left:0;width:1200px}
.tiles{position:absolute;left:135px;top:80px;display:grid;grid-template-columns:repeat(4,218px);grid-template-rows:86px 86px;gap:18px 19px}
.tile{background:var(--tile-bg);display:flex;align-items:center;padding-left:14px;gap:20px;font-size:15px;line-height:19px;color:#222}
.tile-icon{width:58px;height:58px;border-radius:50%;background:var(--icon-blue);display:flex;align-items:center;justify-content:center;flex:none}

/* why choose us */
.why{position:absolute;top:1040px;left:0;width:1200px;height:442px;background:var(--grey-bg)}
.video{position:absolute;left:135px;top:58px;width:408px;height:259px;background:#1c1c1c}
.video-frame{position:absolute;left:0;top:0;width:408px;height:225px;background:linear-gradient(120deg,#d7d4cf,#a9a39b 50%,#ece9e4)}
.video-play{position:absolute;left:174px;top:82px;width:60px;height:60px;border-radius:50%;background:rgba(200,200,200,.8);display:flex;align-items:center;justify-content:center}
.video-bar{position:absolute;left:0;top:225px;width:408px;height:34px;display:flex;align-items:center;gap:10px;padding:0 10px;color:#fff;font-size:12px}
.video-track{flex:1;height:5px;background:#555;border-radius:3px;position:relative}
.video-track:before{content:"";position:absolute;left:0;top:0;width:12%;height:5px;background:#aaa;border-radius:3px}
.why-panel{position:absolute;left:543px;top:33px;width:522px;height:302px;background:var(--white);border-radius:0 40px 40px 0;padding:20px 0 0 38px}
.why-title{font-size:28px;font-weight:700;color:#222}
.why-title span{color:var(--blue)}
.why-sub{font-size:18px;color:#333;margin-top:10px}
.why-list{list-style:none;display:grid;grid-template-columns:240px 240px;row-gap:16px;margin-top:18px;font-size:14px;color:#333;white-space:nowrap}
.why-list li{display:flex;align-items:center;gap:14px}
.buy-now{position:absolute;left:38px;top:222px;width:198px;height:56px;border-radius:8px;background:linear-gradient(#2c87e0,#0b5cb5);color:#fff;font-size:33px;font-weight:700;text-align:center;line-height:56px;box-shadow:0 6px 8px rgba(0,0,0,.25)}
.why-text{position:absolute;left:135px;top:349px;width:930px;text-align:center;font-size:19px;line-height:30px;color:#333}

/* news */
.news{position:absolute;top:1482px;left:0;width:1200px;height:241px;background:linear-gradient(#5b5660,#8f8b93 60%,#b5b3b9)}
.news-item{position:absolute;top:38px;width:432px;color:#fff}
.news-item:first-child{left:135px}
.news-item:last-child{left:643px}
.news-date{font-size:15px;font-weight:700;display:flex;align-items:center;gap:8px}
.news-head{font-size:15px;font-weight:700;margin:12px 0 6px 20px}
.news-body{font-size:14px;line-height:24px;margin-left:20px;color:#d9d7de}
.news-divider{position:absolute;left:599px;top:30px;width:1px;height:180px;background:rgba(255,255,255,.25)}

/* stories */
.stories{position:absolute;top:1723px;left:0;width:1200px;height:413px;background:#e6e6e6}
.stories-head{position:absolute;top:36px;left:165px;width:870px;display:flex;align-items:center;gap:26px}
.stories-head hr{flex:1;border:0;border-top:2px solid #cfcfcf}
.stories-head .section-title{white-space:nowrap}
.story{position:absolute;top:98px;width:280px;text-align:center}
.story-photo{width:111px;height:111px;margin:0 auto;border-radius:32px;border:4px solid #fff;box-shadow:0 0 0 1px #ccc;background:linear-gradient(#8c7a6c,#c9b6a6)}
.story-name{font-size:16px;font-weight:700;color:var(--blue);margin-top:20px}
.story-quote{margin-top:16px;background:#fff;height:104px;padding:16px 18px 0 28px;text-align:left;font-size:13px;font-style:italic;font-weight:700;line-height:22px;color:#555;position:relative}
.story-quote:before{content:"\201C";position:absolute;left:10px;top:8px;font-size:28px;color:#bbb;font-style:normal}

/* footer */
.footer{position:absolute;top:2136px;left:0;width:1200px;height:361px;background:var(--footer);color:#fff}
.footer h3{font-size:18px;font-weight:700}
.quick{position:absolute;left:135px;top:32px;width:275px}
.quick h3{padding-bottom:14px;border-bottom:1px solid #333}
.field{height:31px;background:var(--field);font-size:11px;color:#ccc;padding:9px 10px;margin-top:9px}
.field.msg{height:68px}
.submit{position:absolute;right:0;top:265px;width:91px;height:31px;background:var(--blue);font-size:13px;font-weight:700;text-align:center;line-height:31px;letter-spacing:.5px}
.contact{position:absolute;left:481px;top:32px;width:300px}
.contact h3{padding-bottom:14px}
.contact-row{display:flex;gap:16px;font-size:14px;line-height:21px;margin-top:14px}
.contact-row svg{flex:none;margin-top:2px}
.map{position:absolute;left:784px;top:42px;width:277px;height:277px;border-radius:50%;border:8px solid #2a2a2a;background:radial-gradient(circle at 50% 50%,#ede6c8,#d8e2c4 55%,#a9c6d8)}
.map-leader{position:absolute;left:650px;top:72px}

.footer-low{position:absolute;top:2497px;left:0;width:1200px;height:111px;background:var(--footer-low);color:#fff}
.footer-low h3{font-size:18px;font-weight:700}
.newsletter{position:absolute;left:135px;top:24px}
.newsletter form{display:flex;gap:6px;margin-top:12px}
.newsletter .email{width:248px;height:27px;background:#fff;color:#555;font-size:11px;padding:7px 6px}
.newsletter .go{width:50px;height:27px;background:var(--blue);font-size:13px;font-weight:700;text-align:center;line-height:27px}
.accept{position:absolute;left:535px;top:24px}
.cards{display:flex;gap:8px;margin-top:12px}
.cards span{width:44px;height:30px;border-radius:3px;background:#d9d9d9}
.cards span:nth-child(2){background:#c8c8c8}
.cards span:nth-child(4){background:#e5e5e5}
.cards span:nth-child(5){background:#b9c8d8}
.touch{position:absolute;left:891px;top:24px}
.social{display:flex;gap:16px;margin-top:12px}
.social span{width:32px;height:32px;border-radius:50%;background:#8a8a8a}
.footer-base{position:absolute;top:2608px;left:0;width:1200px;height:54px;background:var(--footer-base);color:#ccc;font-size:13px;text-align:center;line-height:54px}
.footer-base span{margin:0 8px;color:#555}
</style>
</head>
<body>

<nav class="toplinks">
  <ul><li>Home</li><li>Contact</li><li>Trade Application</li><li>About Us</li></ul>
</nav>

<header class="header">
  <div class="brand"><span class="brand-square"></span><span class="brand-name">Brovale CCTV</span></div>
  <div class="hotline">
    <svg width="38" height="38" viewBox="0 0 24 24"><path fill="#222" d="M6.6 10.8a15.1 15.1 0 0 0 6.6 6.6l2.2-2.2a1 1 0 0 1 1-.25 11.4 11.4 0 0 0 3.6.57 1 1 0 0 1 1 1V20a1 1 0 0 1-1 1A17 17 0 0 1 3 4a1 1 0 0 1 1-1h3.5a1 1 0 0 1 1 1c0 1.25.2 2.45.57 3.57a1 1 0 0 1-.25 1z"/></svg>
    <div><div class="hotline-num">020 7946 0381</div><div class="hotline-hours">Mon - Fri 9am - 6pm</div></div>
  </div>
  <div class="search">Search
    <svg width="16" height="16" viewBox="0 0 24 24"><circle cx="10" cy="10" r="6.5" fill="none" stroke="#222" stroke-width="3"/><path d="M15 15l6 6" stroke="#222" stroke-width="3"/></svg>
  </div>
</header>

<nav class="mainnav">
  <ul><li class="active">CCTV CAMERAS</li><li>MONITORS</li><li>SYSTEMS</li><li>HD-SDI</li><li>IP CCTV</li><li>WIRELESS</li><li>ACCESSORIES</li></ul>
  <div class="cart">
    <svg width="24" height="20" viewBox="0 0 24 20"><path d="M1 2h4l3 11h12l3-8H7" fill="none" stroke="#fff" stroke-width="2"/><circle cx="9" cy="17" r="2" fill="#fff"/><circle cx="19" cy="17" r="2" fill="#fff"/></svg>
    Cart: 0 item
  </div>
</nav>

<section class="hero">
  <div class="hero-photo" role="img" aria-label="Bright modern living room interior"></div>
  <div class="hero-camera" role="img" aria-label="Product photo of a bullet CCTV camera"></div>
  <div class="hero-card">
    <div class="hero-kicker"><span class="script">High Quality</span> <span class="accent">Low Price</span></div>
    <div class="hero-title">CCTV CAMERA SYSTEMS</div>
    <p class="hero-text">Lorem ipsum dolor sit amet consectuer adipiscing elit sed diam nonummy nibh euismod</p>
  </div>
</section>

<section class="intro">
  <p>Our CCTV systems have been carefully chosen to give our customers the best possible images at the cheapest prices available on the net. We supply a comprehensive quick set-up guide for all our DVRs and all cables and connectors are included for easy DIY installation.</p>
</section>

<section class="benefits">
  <h2 class="section-title">Benefits Of <span>Our Product</span></h2>
  <div class="tiles">
    <div class="tile"><span class="tile-icon"><svg width="30" height="30" viewBox="0 0 24 24"><circle cx="12" cy="9" r="6" fill="none" stroke="#fff" stroke-width="2"/><path d="M8 14l-2 8 6-3 6 3-2-8" fill="#fff"/></svg></span>2 Year<br>Warranty</div>
    <div class="tile"><span class="tile-icon"><svg width="26" height="30" viewBox="0 0 18 24"><rect x="3" y="1" width="12" height="22" rx="2" fill="#fff"/><rect x="5" y="4" width="8" height="9" fill="#1a5ca6"/></svg></span>Free Telephone<br>Support</div>
    <div class="tile"><span class="tile-icon"><svg width="30" height="30" viewBox="0 0 24 24"><circle cx="12" cy="12" r="10" fill="none" stroke="#fff" stroke-width="2"/><path d="M10 7l6 5-6 5z" fill="#fff"/></svg></span>Plug &amp; Play<br>Technology</div>
    <div class="tile"><span class="tile-icon"><svg width="30" height="30" viewBox="0 0 24 24"><path d="M12 2a10 10 0 1 0 0 20c1.5 0 2-1 1.5-2s0-2 1.5-2h3a4 4 0 0 0 4-4A10 10 0 0 0 12 2z" fill="#fff"/><circle cx="7" cy="11" r="1.6" fill="#1a5ca6"/><circle cx="10" cy="6.5" r="1.6" fill="#1a5ca6"/><circle cx="15" cy="6.5" r="1.6" fill="#1a5ca6"/></svg></span>True<br>Colours</div>
    <div class="tile"><span class="tile-icon"><svg width="30" height="30" viewBox="0 0 24 24"><path d="M2 12L12 3l10 9h-3v9h-5v-6h-4v6H5v-9z" fill="#fff"/></svg></span>Indoor<br>Use</div>
    <div class="tile"><span class="tile-icon"><svg width="30" height="30" viewBox="0 0 24 24"><path d="M12 2l6 8h-3l5 7h-7v5h-2v-5H4l5-7H6z" fill="#fff"/></svg></span>Outdoor<br>Use</div>
    <div class="tile"><span class="tile-icon"><svg width="26" height="30" viewBox="0 0 18 24"><rect x="3" y="1" width="12" height="22" rx="2" fill="#fff"/><circle cx="9" cy="19" r="1.4" fill="#1a5ca6"/></svg></span>Smartphone<br>Compatible</div>
    <div class="tile"><span class="tile-icon"><svg width="30" height="30" viewBox="0 0 24 24"><path d="M3 9h4l5-4v14l-5-4H3z" fill="#fff"/><path d="M4 21L20 4" stroke="#fff" stroke-width="2"/></svg></span>Silent<br>Running</div>
  </div>
</section>

<section class="why">
  <div class="video">
    <div class="video-frame" role="img" aria-label="Video still of a man working at a laptop"></div>
    <div class="video-play"><svg width="24" height="26" viewBox="0 0 24 26"><path d="M4 2l18 11L4 24z" fill="#fff"/></svg></div>
    <div class="video-bar">
      <svg width="12" height="12" viewBox="0 0 12 12"><path d="M1 0l11 6-11 6z" fill="#fff"/></svg>
      <span>04:59</span><span class="video-track"></span><span>10:35</span>
      <svg width="14" height="12" viewBox="0 0 14 12"><path d="M0 4h3l4-3v10l-4-3H0z" fill="#fff"/></svg>
      <svg width="12" height="12" viewBox="0 0 12 12"><path d="M0 4V0h4M8 0h4v4M12 8v4H8M4 12H0V8" fill="none" stroke="#fff" stroke-width="1.5"/></svg>
    </div>
  </div>
  <div class="why-panel">
    <h2 class="why-title">Why <span>Choose Us</span></h2>
    <p class="why-sub">Diam nonummy nibh euismodt laoreet dolore magna</p>
    <ul class="why-list">
      <li><svg width="13" height="11" viewBox="0 0 13 11"><path d="M1 6l4 4 7-9" fill="none" stroke="#444" stroke-width="2"/></svg>Lorem Ipsum Dolor Ame</li>
      <li><svg width="13" height="11" viewBox="0 0 13 11"><path d="M1 6l4 4 7-9" fill="none" stroke="#444" stroke-width="2"/></svg>Exdea Commodo Consequat</li>
      <li><svg width="13" height="11" viewBox="0 0 13 11"><path d="M1 6l4 4 7-9" fill="none" stroke="#444" stroke-width="2"/></svg>Nonummy Nibh Euismod</li>
      <li><svg width="13" height="11" viewBox="0 0 13 11"><path d="M1 6l4 4 7-9" fill="none" stroke="#444" stroke-width="2"/></svg>Dol Magna Aliquam Erat</li>
      <li><svg width="13" height="11" viewBox="0 0 13 11"><path d="M1 6l4 4 7-9" fill="none" stroke="#444" stroke-width="2"/></svg>Dolore Magna Aliquam</li>
      <li><svg width="13" height="11" viewBox="0 0 13 11"><path d="M1 6l4 4 7-9" fill="none" stroke="#444" stroke-width="2"/></svg>Aliquip Ex Ea Commodo Coqu</li>
    </ul>
    <a class="buy-now" href="#">BUY NOW</a>
  </div>
  <p class="why-text">Lorem ipsum dolor sit amet, consectetuer adipiscing elit, sed diam nonummy nibh euismod tincidunt ut laoreet dolore magna aliquam erat volutpat. Ut wisi enim ad minim veniam.</p>
</section>

<section class="news">
  <article class="news-item">
    <div class="news-date"><svg width="13" height="13" viewBox="0 0 13 13"><rect x="0" y="2" width="13" height="11" fill="#fff"/></svg>14-March-2014</div>
    <h4 class="news-head">Exerci tation ullamcorper suscipit lobortis nisl ut aliquip.</h4>
    <p class="news-body">Lorem ipsum dolor sit amet ctuer adipiscing ed diam nonumy nibh eud tincidunt ut laoreet dol magna aliquam erat volutpat wisi enim ad minim veniam, quis nostrud exerci tation urper suscipit lobortis nisl ut aliquip ex ea commodo consequat.</p>
  </article>
  <span class="news-divider"></span>
  <article class="news-item">
    <div class="news-date"><svg width="13" height="13" viewBox="0 0 13 13"><rect x="0" y="2" width="13" height="11" fill="#fff"/></svg>21-March-2014</div>
    <h4 class="news-head">Exerci tation ullamcorper suscipit lobortis nisl ut aliquip.</h4>
    <p class="news-body">Lorem ipsum dolor sit amet ctuer adipiscing ed diam nonumy nibh eud tincidunt ut laoreet dol magna aliquam erat volutpat wisi enim ad minim veniam, quis nostrud exerci tation urper suscipit lobortis nisl ut aliquip ex ea commodo consequat.</p>
  </article>
</section>

<section class="stories">
  <div class="stories-head"><hr><h2 class="section-title">Some <span>Success Stories</span></h2><hr></div>
  <div class="story" style="left:135px">
    <div class="story-photo" role="img" aria-label="Customer portrait"></div>
    <div class="story-name">Neil Arden</div>
    <p class="story-quote">Lorem ipsum dolor sit co adipiscig elitsed do eiusmod tepor incidunt ut la dolore magna alique enim nim veni exercitation ullamco</p>
  </div>
  <div class="story" style="left:460px">
    <div class="story-photo" role="img" aria-label="Customer portrait"></div>
    <div class="story-name">Tom Realby</div>
    <p class="story-quote">Lorem ipsum dolor sit co adipiscig elitsed do eiusmod tepor incidunt ut la dolore magna alique enim nim veni exercitation ullamco</p>
  </div>
  <div class="story" style="left:785px">
    <div class="story-photo" role="img" aria-label="Customer portrait"></div>
    <div class="story-name">Lena Marsh</div>
    <p class="story-quote">Lorem ipsum dolor sit co adipiscig elitsed do eiusmod tepor incidunt ut la dolore magna alique enim nim veni exercitation ullamco</p>
  </div>
</section>

<footer class="footer">
  <div class="quick">
    <h3>Quick Contact</h3>
    <div class="field">Name</div>
    <div class="field">Email</div>
    <div class="field">Phone</div>
    <div class="field msg">Message</div>
    <span class="submit">SUBMIT</span>
  </div>
  <div class="contact">
    <h3>Contact information</h3>
    <div class="contact-row"><svg width="26" height="26" viewBox="0 0 24 24"><circle cx="12" cy="12" r="10" fill="none" stroke="#fff" stroke-width="2"/><path d="M12 6v6h5" fill="none" stroke="#fff" stroke-width="2"/></svg><span>Open everyday<br>from 12a.m. to 2:15p.m.<br>and 6p.m. to midnight</span></div>
    <div class="contact-row"><svg width="26" height="26" viewBox="0 0 24 24"><path d="M12 2a7 7 0 0 0-7 7c0 5 7 13 7 13s7-8 7-13a7 7 0 0 0-7-7z" fill="#fff"/><circle cx="12" cy="9" r="2.5" fill="#151515"/></svg><span>123 Lorem ipsum sitamet<br>co adipiscig adipiscig<br>Eilsed</span></div>
    <div class="contact-row" style="font-size:17px"><svg width="26" height="22" viewBox="0 0 24 24"><path d="M6.6 10.8a15.1 15.1 0 0 0 6.6 6.6l2.2-2.2a1 1 0 0 1 1-.25 11.4 11.4 0 0 0 3.6.57 1 1 0 0 1 1 1V20a1 1 0 0 1-1 1A17 17 0 0 1 3 4a1 1 0 0 1 1-1h3.5a1 1 0 0 1 1 1c0 1.25.2 2.45.57 3.57a1 1 0 0 1-.25 1z" fill="#fff"/></svg><span>123-456-789</span></div>
    <div class="contact-row"><svg width="26" height="18" viewBox="0 0 24 16"><rect x="1" y="1" width="22" height="14" fill="#fff"/><path d="M1 1l11 8 11-8" fill="none" stroke="#151515" stroke-width="1.5"/></svg><span>info@brovalemount-mail.com</span></div>
  </div>
  <svg class="map-leader" width="140" height="40" viewBox="0 0 140 40"><path d="M2 20c40 -14 90 -14 136 0" stroke="#777" stroke-width="1.5" fill="none"/><path d="M2 20l10-7v10z" fill="#777"/></svg>
  <div class="map" role="img" aria-label="Street map showing the shop location"></div>
</footer>

<section class="footer-low">
  <div class="newsletter">
    <h3>Newsletter Signup</h3>
    <form><span class="email">Enter your email.....</span><span class="go">GO</span></form>
  </div>
  <div class="accept">
    <h3>We Accept</h3>
    <div class="cards"><span></span><span></span><span></span><span></span><span></span></div>
  </div>
  <div class="touch">
    <h3>Stay in Touch</h3>
    <div class="social"><span></span><span></span><span></span><span></span></div>
  </div>
</section>

<div class="footer-base">© 2014 Brovalemount | All Rights Reserved<span>|</span>Terms and conditions</div>

</body>
</html>
```